Bref créative
Bright Harbor Solutions
Business card template
Modern
Derek Tolland
812 Birchfield Rd
Wayne NJ 07512
dtolland@brightharborsolutions.example
www.BrightHarborSolutions.example
Rounded corners, use icons instead of words for phone, email, etc..
I like the idea of my "e" logo as a feint watermark as part of the background, but it's not critical. Maybe blacks and blues?
Web address should include caps "www.BrightHarborSolutions.example". Maybe Network could be a slightly different color so the address doesnt look run on.
Black background, maybe some sort of subtle gradiant. Logo in the upper center. Web address on the bottom. I also would like an editable layer where I can add (4 or 6) up to 20 character services that I provide. example: "Custom Wall Fishing" "Home Theater Setup". "Security Cameras" "Structured Wiring"

```html
<!DOCTYPE html>
<html lang="en">
<head>
<meta charset="utf-8">
<title>Bright Harbor Solutions – Business Card</title>
<link rel="stylesheet" href="https://fonts.googleapis.com/css2?family=Source+Sans+3:wght@400;600;700&family=Cormorant+Garamond:wght@500&display=swap">
<style>
  :root {
    --stage: #e9e6e2;
    --card-white: #ffffff;
    --card-grey: #e6e9ec;
    --brand-blue: #1b8fd2;
    --brand-blue-light: #3aaee6;
    --brand-blue-deep: #0b5d96;
    --ink: #1d2530;
    --muted: #8b939c;
    --label: #3b3b3b;
  }
  * { margin: 0; padding: 0; box-sizing: border-box; }
  html, body { width: 1200px; height: 929px; overflow: hidden; }
  body {
    background: var(--stage);
    font-family: "Source Sans 3", Arial, sans-serif;
    position: relative;
  }
  .card {
    position: absolute;
    left: 250px;
    width: 560px;
    height: 320px;
    border-radius: 28px;
    overflow: hidden;
    box-shadow: 0 14px 34px rgba(0,0,0,0.22);
  }
  .card--front {
    top: 90px;
    background: linear-gradient(180deg, var(--card-white) 0%, var(--card-white) 45%, var(--card-grey) 100%);
  }
  .card--back {
    top: 510px;
    background: radial-gradient(ellipse at 40% 35%, var(--brand-blue-light) 0%, var(--brand-blue) 45%, var(--brand-blue-deep) 100%);
  }
  .brand {
    position: absolute;
    display: flex;
    align-items: center;
    gap: 12px;
  }
  .brand__dot {
    width: 50px; height: 50px;
    border-radius: 50%;
    background: #a9b2ba;
    flex: none;
  }
  .brand__name {
    font-weight: 600;
    font-size: 27px;
    line-height: 1.05;
    color: var(--brand-blue);
  }
  .card--front .brand { left: 34px; top: 104px; }
  .card--front .brand__name { width: 190px; }
  .card--back .brand { left: 50%; top: 50%; transform: translate(-50%, -50%); }
  .card--back .brand__dot { background: #d6dde3; }
  .card--back .brand__name { color: #ffffff; }

  .contact {
    position: absolute;
    left: 320px;
    top: 38px;
    color: var(--ink);
  }
  .contact__name {
    font-weight: 600;
    font-size: 27px;
    color: var(--brand-blue-deep);
    margin-bottom: 8px;
  }
  .contact__row {
    display: flex;
    align-items: flex-start;
    gap: 8px;
    font-size: 15px;
    font-weight: 600;
    line-height: 1.3;
  }
  .contact__address { margin-bottom: 6px; }
  .contact__row svg { width: 14px; height: 14px; margin-top: 3px; flex: none; fill: var(--ink); }

  .footer-band {
    position: absolute;
    left: 0; right: 0; bottom: 0;
    height: 78px;
    background: linear-gradient(180deg, var(--brand-blue-light) 0%, var(--brand-blue) 100%);
  }
  .footer-line {
    position: absolute;
    left: 0; right: 0; bottom: 78px;
    height: 40px;
    display: flex;
    align-items: center;
    gap: 18px;
    padding-left: 26px;
    font-size: 13px;
    color: var(--ink);
    white-space: nowrap;
  }
  .footer-line span { display: flex; align-items: center; gap: 5px; }
  .footer-line svg { width: 13px; height: 13px; fill: var(--ink); }

  .side-label {
    position: absolute;
    left: 870px;
    font-family: "Cormorant Garamond", Georgia, serif;
    font-weight: 500;
    font-size: 30px;
    letter-spacing: 1px;
    color: var(--label);
  }
  .side-label--front { top: 150px; }
  .side-label--back { top: 570px; }
</style>
</head>
<body>

  <section class="card card--front" aria-label="Card front">
    <div class="brand">
      <div class="brand__dot"></div>
      <div class="brand__name">Bright Harbor Solutions</div>
    </div>

    <div class="contact">
      <div class="contact__name">Derek Tolland</div>
      <div class="contact__row contact__address">
        <svg viewBox="0 0 16 16" aria-hidden="true"><path d="M8 1 1 7h2v7h4v-4h2v4h4V7h2z"/></svg>
        <div>812 Birchfield Rd<br>Wayne NJ 07512</div>
      </div>
      <div class="contact__row">
        <svg viewBox="0 0 16 16" aria-hidden="true"><path d="M4 1l3 3-2 2c1 2 3 4 5 5l2-2 3 3-2 3C7 15 1 9 1 3z"/></svg>
        <div>1-888-555-0142</div>
      </div>
      <div class="contact__row">
        <svg viewBox="0 0 16 16" aria-hidden="true"><path d="M4 0h8v16H4zM5.5 2v10h5V2zM7 13h2v1.5H7z"/></svg>
        <div>973-555-0187</div>
      </div>
      <div class="contact__row">
        <svg viewBox="0 0 16 16" aria-hidden="true"><path d="M4 1h7v4H4zM1 6h14v7h-3v2H4v-2H1zM5 10v4h6v-4z"/></svg>
        <div>973-555-0110</div>
      </div>
    </div>

    <div class="footer-line">
      <span>
        <svg viewBox="0 0 16 16" aria-hidden="true"><path d="M1 3h14v10H1zM2.5 4.5 8 9l5.5-4.5z"/></svg>
        dtolland@brightharborsolutions.example
      </span>
      <span>
        <svg viewBox="0 0 16 16" aria-hidden="true"><path d="M8 1a7 7 0 1 0 0 14A7 7 0 0 0 8 1zm0 1.5c.8 0 1.7 1.9 1.9 4.5H6.1C6.3 4.4 7.2 2.5 8 2.5zM2.6 7h2c.1-1.6.4-3 .9-3.9A5.5 5.5 0 0 0 2.6 7zm8.8 0h2a5.5 5.5 0 0 0-2.9-3.9c.5.9.8 2.3.9 3.9zM2.6 9a5.5 5.5 0 0 0 2.9 3.9c-.5-.9-.8-2.3-.9-3.9zm3.5 0c.2 2.6 1.1 4.5 1.9 4.5s1.7-1.9 1.9-4.5zm5.3 0c-.1 1.6-.4 3-.9 3.9A5.5 5.5 0 0 0 13.4 9z"/></svg>
        www.BrightHarborSolutions.example
      </span>
    </div>
    <div class="footer-band"></div>
  </section>

  <div class="side-label side-label--front">FRONT</div>

  <section class="card card--back" aria-label="Card back">
    <div class="brand">
      <div class="brand__dot"></div>
      <div class="brand__name">Bright Harbor Solutions</div>
    </div>
  </section>

  <div class="side-label side-label--back">BACK</div>

</body>
</html>
```